CD Cover Artwork for Classical Music Cover

We are about to launch 13 CDs online for digital downloads and require artwork for the accompanying CD covers. As the covers will not be printed, we only require web-optimized artwork. We are fine with one standard template that can be adapted for all the covers. The only differentiating factors will be the colour of the covers and the title information. We need to create a more progressive, eye-catching design than the below examples which we have been promoting through our website until now. You have full liberties to come up with whatever design you think is more appropriate and to use whatever fonts and juxtaposition of content and images as you see fit.
ARTIST INFORMATION: Harold Venmark was an American composer who lived and worked his entire life in New York City. He was a 1930 Marlowe Conservatory graduate and studied composition with Milton Brasher, Lew Doddard, Pemberton Quillock and Walter Pennimore. In a 1947 competition, with Karl Estergaard as one of three jurors, Venmark’s "Harbor Prelude" won First Prize. He produced a large body of work comprising hundreds of compositions across diverse musical genres ... From 2001 to early 2008, Harold Venmark’s music came to life through a unique collaboration with many of the finest musicians in St. Petersburg, Russia. Nearly all of Venmark’s musical repertoire was transcribed from their original manuscripts to electronic form. And dozens of recording sessions produced 13 CDs, including all his chambers works, many piano concertos and symphonies, and works for horn, flute, strings and woodwinds. This “musical discovery” was the brainchild of his late son, Thomas Venmark.
ARTIST WEBSITE: www.haroldvenmark.com
FACEBOOK PAGE: https://www.facebook.com/pages/Harold-Venmark-A-Hidden-Chapter-of-Concert-Song/582910374615208
ATTACHMENTS:
- A few images of Harold Venmark (young and old)
- List of CD information along with a visual representation of the information that should be included
Target Market(s)
Classical music lovers the world over
Industry/Entity Type
Electronic
Look and feel

```html
<!DOCTYPE html>
<html lang="en">
<head>
<meta charset="utf-8">
<title>Harold Venmark – Cover Series</title>
<link rel="stylesheet" href="https://fonts.googleapis.com/css2?family=Archivo+Black&family=Archivo:wght@400;600;700;800&family=Parisienne&display=swap">
<style>
  :root {
    --stage-light: #fdfcf8;
    --stage-mid: #e6e5e1;
    --stage-edge: #8f8f8f;
    --ink-light: #e4dfd4;
    --title-red: #c41d0d;
    --band: #e8e6e1;
    --band-shadow: rgba(0,0,0,0.35);
    --cover-black: #111111;
    --dates-grey: #3c3c3c;
    --c01: #c51b0a;
    --c02: #1e8aa8;
    --c03: #458605;
    --c04: #95447f;
    --c05: #dc7003;
    --c06: #0049a0;
    --c07: #cc9040;
    --c08: #9c053c;
    --c09: #8a8a1c;
    --c10: #7a330c;
    --c11: #a88e68;
    --c12: #068577;
    --c14: #b02e35;
  }
  * { box-sizing: border-box; margin: 0; padding: 0; }
  html, body { width: 1200px; height: 900px; overflow: hidden; }
  body {
    position: relative;
    background: radial-gradient(ellipse 62% 62% at 50% 45%, var(--stage-light) 0%, var(--stage-light) 35%, var(--stage-mid) 70%, var(--stage-edge) 100%);
    font-family: "Archivo", Arial, sans-serif;
  }

  /* Featured cover */
  .cover {
    position: absolute;
    left: 57px; top: 113px;
    width: 538px; height: 537px;
    background: var(--cover-black);
    overflow: hidden;
  }
  .cover__photo {
    position: absolute;
    left: 0; top: 120px; width: 100%; height: 417px;
    background:
      radial-gradient(ellipse 40% 45% at 65% 55%, #8a8a88 0%, #3a3a39 45%, transparent 80%),
      radial-gradient(ellipse 55% 30% at 45% 85%, #6b6b69 0%, transparent 70%),
      #0c0c0c;
  }
  .cover__band {
    position: absolute;
    left: 0; top: 22px; width: 100%; height: 100px;
    background: var(--band);
    box-shadow: 0 4px 6px var(--band-shadow);
  }
  .cover__tab {
    position: absolute;
    left: 28px; top: 10px;
    width: 96px; height: 121px;
    background: var(--c01);
    color: var(--ink-light);
    text-align: center;
  }
  .cover__tab-number {
    display: block;
    margin-top: 18px;
    font-family: "Archivo Black", Arial, sans-serif;
    font-size: 33px;
    line-height: 1;
  }
  .cover__tab-label {
    display: block;
    margin-top: 43px;
    font-weight: 700;
    font-size: 12px;
    line-height: 1.02;
  }
  .cover__heading {
    position: absolute;
    right: 30px; top: 36px;
    text-align: right;
  }
  .cover__name {
    font-family: "Archivo Black", Arial, sans-serif;
    font-size: 27px;
    letter-spacing: 0.5px;
    color: var(--title-red);
    line-height: 1;
  }
  .cover__dates {
    margin-top: 3px;
    font-size: 15px;
    color: var(--dates-grey);
  }
  .cover__tagline {
    margin-top: 2px;
    font-weight: 700;
    font-size: 15px;
    font-variant: small-caps;
    letter-spacing: 0.6px;
    color: #262626;
  }
  .cover__series {
    position: absolute;
    left: 90px; top: 148px;
    font-family: "Parisienne", cursive;
    font-size: 30px;
    letter-spacing: 2px;
    color: var(--title-red);
    opacity: 0.85;
  }

  /* Series tiles */
  .tile {
    position: absolute;
    width: 151px; height: 194px;
    color: var(--ink-light);
    text-align: center;
  }
  .tile__number {
    display: block;
    margin-top: 34px;
    font-family: "Archivo Black", Arial, sans-serif;
    font-size: 56px;
    line-height: 1;
    text-shadow: 0 1px 2px rgba(0,0,0,0.25);
  }
  .tile__label {
    display: block;
    margin-top: 46px;
    font-weight: 700;
    font-size: 18px;
    line-height: 1;
  }
  .tile--01 { background: var(--c01); }
  .tile--02 { background: var(--c02); }
  .tile--03 { background: var(--c03); }
  .tile--04 { background: var(--c04); }
  .tile--05 { background: var(--c05); }
  .tile--06 { background: var(--c06); }
  .tile--07 { background: var(--c07); }
  .tile--08 { background: var(--c08); }
  .tile--09 { background: var(--c09); }
  .tile--10 { background: var(--c10); }
  .tile--11 { background: var(--c11); }
  .tile--12 { background: var(--c12); }
  .tile--14 { background: var(--c14); }
</style>
</head>
<body>

  <section class="cover" aria-label="Volume 01 cover">
    <div class="cover__photo" role="img" aria-label="Black and white photograph of the composer writing at a desk under a lamp"></div>
    <div class="cover__band"></div>
    <div class="cover__tab">
      <span class="cover__tab-number">01</span>
      <span class="cover__tab-label">Halvern<br>Publishing</span>
    </div>
    <div class="cover__heading">
      <h1 class="cover__name">HAROLD VENMARK</h1>
      <p class="cover__dates">(1905-1986)</p>
      <p class="cover__tagline">A Hidden Chapter of Concert Song</p>
    </div>
    <p class="cover__series">Selected Chamber Works</p>
  </section>

  <div class="tile tile--02" style="left:619px;top:16px"><span class="tile__number">02</span><span class="tile__label">Halvern<br>Publishing</span></div>
  <div class="tile tile--03" style="left:810px;top:16px"><span class="tile__number">03</span><span class="tile__label">Halvern<br>Publishing</span></div>
  <div class="tile tile--04" style="left:1000px;top:16px"><span class="tile__number">04</span><span class="tile__label">Halvern<br>Publishing</span></div>

  <div class="tile tile--05" style="left:619px;top:238px"><span class="tile__number">05</span><span class="tile__label">Halvern<br>Publishing</span></div>
  <div class="tile tile--06" style="left:810px;top:238px"><span class="tile__number">06</span><span class="tile__label">Halvern<br>Publishing</span></div>
  <div class="tile tile--07" style="left:1000px;top:238px"><span class="tile__number">07</span><span class="tile__label">Halvern<br>Publishing</span></div>

  <div class="tile tile--08" style="left:619px;top:462px"><span class="tile__number">08</span><span class="tile__label">Halvern<br>Publishing</span></div>
  <div class="tile tile--09" style="left:810px;top:462px"><span class="tile__number">09</span><span class="tile__label">Halvern<br>Publishing</span></div>
  <div class="tile tile--10" style="left:1000px;top:462px"><span class="tile__number">10</span><span class="tile__label">Halvern<br>Publishing</span></div>

  <div class="tile tile--01" style="left:435px;top:692px"><span class="tile__number">01</span><span class="tile__label">Halvern<br>Publishing</span></div>
  <div class="tile tile--11" style="left:619px;top:692px"><span class="tile__number">11</span><span class="tile__label">Halvern<br>Publishing</span></div>
  <div class="tile tile--12" style="left:810px;top:692px"><span class="tile__number">12</span><span class="tile__label">Halvern<br>Publishing</span></div>
  <div class="tile tile--14" style="left:1000px;top:692px"><span class="tile__number">14</span><span class="tile__label">Halvern<br>Publishing</span></div>

</body>
</html>
```